Plantwise Mechanics Partners. Needs a Business Card Design

We need a business card design for an engineering company which supplies industrial components (pumps, compressors, mechanical seals) provides repairs and services for above mentioned equipments. We offer a uniqe engineering solutions which help our customers to increase the productivness of their manufacturings, and energy savings.

Target Market(s)

Chemical and energy plants, refineries. Food industry and private consumers in a less.

Industry/Entity Type

Business

Contact Information for Business Card

Stylish and sleek design oriented on industrial area.

Requirements
Should not have
• company name shortening

```html
<!DOCTYPE html>
<html lang="en">
<head>
<meta charset="utf-8">
<title>Plantwise Mechanics Partners – Business Cards</title>
<link rel="stylesheet" href="https://fonts.googleapis.com/css2?family=Ubuntu:wght@400;500;700&display=swap">
<style>
  :root{
    --page:#e9e6e1;
    --card-dark:#1a1a1a;
    --card-dark-centre:#2a2a2a;
    --grid-dark:rgba(255,255,255,.06);
    --grid-dark-major:rgba(255,255,255,.09);
    --card-light:#f5f3ef;
    --card-light-edge:#e8e5df;
    --grid-light:rgba(60,60,60,.07);
    --grid-light-major:rgba(60,60,60,.11);
    --sketch-dark:rgba(255,255,255,.07);
    --sketch-light:rgba(90,90,90,.09);
    --ink:#1b1b1b;
    --ink-white:#ffffff;
    --accent:#2a4aa8;
    --muted:#333333;
  }
  *{margin:0;padding:0;box-sizing:border-box}
  html,body{width:1200px;height:784px;overflow:hidden}
  body{
    background:var(--page);
    font-family:"Ubuntu",Arial,sans-serif;
    position:relative;
  }
  .card{
    position:absolute;
    top:222px;
    width:540px;
    height:320px;
    border-radius:4px;
    overflow:hidden;
    box-shadow:0 10px 28px rgba(0,0,0,.18);
  }
  .card--front{
    left:40px;
    background:radial-gradient(ellipse at 50% 40%,var(--card-dark-centre),var(--card-dark) 75%);
  }
  .card--back{
    left:620px;
    background:linear-gradient(135deg,var(--card-light),var(--card-light-edge));
  }

  /* blueprint grid */
  .card__grid{position:absolute;inset:0}
  .card--front .card__grid{
    background-image:
      linear-gradient(var(--grid-dark-major) 1px,transparent 1px),
      linear-gradient(90deg,var(--grid-dark-major) 1px,transparent 1px),
      linear-gradient(var(--grid-dark) 1px,transparent 1px),
      linear-gradient(90deg,var(--grid-dark) 1px,transparent 1px);
    background-size:40px 40px,40px 40px,8px 8px,8px 8px;
  }
  .card--back .card__grid{
    background-image:
      linear-gradient(var(--grid-light-major) 1px,transparent 1px),
      linear-gradient(90deg,var(--grid-light-major) 1px,transparent 1px),
      linear-gradient(var(--grid-light) 1px,transparent 1px),
      linear-gradient(90deg,var(--grid-light) 1px,transparent 1px);
    background-size:36px 36px,36px 36px,18px 18px,18px 18px;
  }

  /* technical sketch areas, kept as soft tone */
  .card__sketch{position:absolute;border-radius:50%}
  .card--front .card__sketch{background:radial-gradient(circle,var(--sketch-dark),transparent 70%)}
  .card--back .card__sketch{background:radial-gradient(circle,var(--sketch-light),transparent 70%)}
  .sketch--front-left{left:-60px;top:60px;width:300px;height:300px}
  .sketch--front-right{right:-40px;top:120px;width:240px;height:240px}
  .sketch--back-left{left:-50px;top:150px;width:280px;height:280px}
  .sketch--back-right{right:-30px;top:40px;width:260px;height:260px}

  .card__content{position:absolute;inset:0}

  .brand-dot{
    position:absolute;
    left:50%;
    width:46px;height:46px;
    margin-left:-23px;
    border-radius:50%;
    background:var(--accent);
  }
  .card--front .brand-dot{top:70px}
  .card--back .brand-dot{top:74px}

  .brand-name{
    position:absolute;
    left:0;right:0;
    text-align:center;
    font-weight:700;
    letter-spacing:.2px;
    white-space:nowrap;
  }
  .card--front .brand-name{top:132px;font-size:30px;color:var(--ink-white)}
  .card--back .brand-name{top:134px;font-size:30px;color:var(--ink)}

  .person{position:absolute;top:18px;right:24px;text-align:right}
  .person__name{font-weight:700;font-size:15px;color:var(--accent);letter-spacing:.3px}
  .person__role{font-size:10px;color:var(--muted);margin-top:1px}

  .contact-list{position:absolute;left:24px;bottom:16px;list-style:none}
  .contact-list__item{
    display:flex;align-items:center;gap:8px;
    height:19px;font-size:13px;font-weight:500;color:var(--ink);
    white-space:nowrap;
  }
  .contact-list__icon{width:13px;height:13px;flex:none;fill:var(--accent)}
  .contact-list__item--plain{padding-left:21px}
</style>
</head>
<body>

  <section class="card card--front" aria-label="Business card front">
    <div class="card__grid"></div>
    <div class="card__sketch sketch--front-left" role="img" aria-label="Faint technical drawing of gears and machine parts"></div>
    <div class="card__sketch sketch--front-right" role="img" aria-label="Faint technical drawing of a pump housing"></div>
    <div class="card__content">
      <span class="brand-dot"></span>
      <p class="brand-name">Plantwise Mechanics Partners</p>
    </div>
  </section>

  <section class="card card--back" aria-label="Business card back">
    <div class="card__grid"></div>
    <div class="card__sketch sketch--back-left" role="img" aria-label="Faint pencil sketch of a flange and bearing"></div>
    <div class="card__sketch sketch--back-right" role="img" aria-label="Faint pencil sketch of a compressor assembly"></div>
    <div class="card__content">
      <div class="person">
        <p class="person__name">DANA MERROW</p>
        <p class="person__role">Manager</p>
      </div>

      <span class="brand-dot"></span>
      <p class="brand-name">Plantwise Mechanics Partners</p>

      <ul class="contact-list">
        <li class="contact-list__item">
          <svg class="contact-list__icon" viewBox="0 0 16 16" aria-hidden="true"><rect x="4" y="1" width="8" height="14" rx="1.5"/><rect x="5.5" y="3" width="5" height="8" fill="#fff"/></svg>
          0412 555 208
        </li>
        <li class="contact-list__item">
          <svg class="contact-list__icon" viewBox="0 0 16 16" aria-hidden="true"><path d="M2 5c0-2 2-3 6-3s6 1 6 3v1.5h-3.5V5h-5v1.5H2z"/><rect x="3" y="8" width="10" height="6" rx="1"/></svg>
          +61 7 3555 0147
        </li>
        <li class="contact-list__item">
          <svg class="contact-list__icon" viewBox="0 0 16 16" aria-hidden="true"><rect x="1" y="3" width="14" height="10" rx="1"/><path d="M2 4l6 5 6-5" fill="none" stroke="#fff" stroke-width="1.4"/></svg>
          dana@plantwisemechanics.com
        </li>
        <li class="contact-list__item">
          <svg class="contact-list__icon" viewBox="0 0 16 16" aria-hidden="true"><circle cx="8" cy="8" r="7"/><path d="M1 8h14M8 1c-3 3-3 11 0 14M8 1c3 3 3 11 0 14" fill="none" stroke="#fff" stroke-width="1"/></svg>
          www.plantwisemechanics.com
        </li>
        <li class="contact-list__item">
          <svg class="contact-list__icon" viewBox="0 0 16 16" aria-hidden="true"><path d="M8 1L1 8h2v7h4v-4h2v4h4V8h2z"/></svg>
          14 Harlow Street Northgate
        </li>
        <li class="contact-list__item contact-list__item--plain">ABN 10 000 000 000</li>
      </ul>
    </div>
  </section>

</body>
</html>
```